WIX DESIGN AND CODED - Corvane Asset Management

Use logo source code files..golden or silver M etc in design

we manage money for rich people - its a private wealth management firm

It is for High Net Wealth clients only and gives them access to off market opportunities like 5 star hotels. It needs that look and feel that we look after the wealth of millionaires and above as a exclusive club. Based in Melbourne. projects in Melbourne, Shanghai and US and Singapore and Hong Kong.

looks Regal

Target Market(s)

rich people from asia and across the globe

https://www.trellowaybank.com/ - here is a nice simple one to improve on!

e.g. see landing page or page 1 of www.harnfieldgroup.com

look clean - not information overload

Industry/Entity Type

Investment Advisory

Coding

Coded - Design and coding required

Font styles to use
Serif
Sans Serif

Colors

Designer to choose colors to be used in the design.

Requirements
Must have
• https://www.trellowaybank.com/ - really good website i would " reference" - be it the layout - tabs - etc - obviously add your own flare and colour scheme to make it look posh
• look like we are a rich company and manage rich peoples money
• money will go into private, off market deals that you can just buy online or from your local financial planner
• some animation - e.g. quotes or pictures that scroll or refresh every 5 seconds
Nice to have
• format so that it works if viewed from computer or mobile phone
Should not have
• no cartoons - this is a serious website for people with serious money :)

```html
<!DOCTYPE html>
<html lang="en">
<head>
<meta charset="utf-8">
<title>Corvane Asset Management</title>
<link href="https://fonts.googleapis.com/css2?family=Exo+2:wght@400;500;600&display=swap" rel="stylesheet">
<style>
  :root {
    --ink: #221c38;
    --ink-soft: #2b2540;
    --white: #ffffff;
    --gold: #c8963f;
    --sun: #fff3d6;
    --amber: #f2c783;
    --sage: #9fb36a;
    --forest: #4f6a3a;
    --dusk: #4b5358;
    --wood-light: #b59a83;
    --wood-dark: #4a3a34;
  }
  * { margin: 0; padding: 0; box-sizing: border-box; }
  html, body { width: 1200px; height: 814px; overflow: hidden; }
  body { font-family: "Exo 2", sans-serif; color: var(--ink); }

  .hero { position: relative; width: 1200px; height: 814px; overflow: hidden; }

  .hero-photo {
    position: absolute; inset: 0;
    background:
      linear-gradient(180deg, rgba(0,0,0,0) 74%, var(--wood-light) 77%, #8c7262 88%, var(--wood-dark) 100%),
      radial-gradient(circle at 12% 8%, var(--sun) 0%, rgba(255,243,214,0.9) 14%, rgba(242,199,131,0.6) 34%, rgba(242,199,131,0) 58%),
      radial-gradient(ellipse at 88% 50%, #6e8a3e 0%, rgba(110,138,62,0.7) 30%, rgba(110,138,62,0) 60%),
      linear-gradient(100deg, var(--amber) 0%, #e9c79b 35%, var(--sage) 62%, var(--forest) 82%, var(--dusk) 100%);
  }
  .hero-object {
    position: absolute; left: 686px; top: 166px; width: 456px; height: 530px;
    background: radial-gradient(ellipse at 48% 70%, rgba(120,84,50,0.75) 0%, rgba(120,84,50,0.45) 40%, rgba(120,84,50,0) 70%);
  }

  .brand { position: absolute; left: 74px; top: 56px; display: flex; align-items: center; gap: 16px; color: var(--ink-soft); font-weight: 400; }
  .brand-mark { width: 44px; height: 44px; background: var(--gold); }
  .brand-name { display: flex; flex-direction: column; }
  .brand-name .word { font-size: 48px; letter-spacing: 5px; line-height: 44px; }
  .brand-name .sub { font-size: 11px; letter-spacing: 8.6px; margin-top: 4px; }

  .investor-login {
    position: absolute; right: 68px; top: 67px;
    font-size: 12.5px; font-weight: 500; letter-spacing: 1.2px; color: var(--white); text-decoration: none;
  }
  .main-nav { position: absolute; right: 68px; top: 102px; display: flex; align-items: center; gap: 15px; }
  .main-nav a { color: var(--white); text-decoration: none; font-size: 15px; font-weight: 500; }
  .main-nav .sep { color: var(--white); font-size: 15px; font-weight: 500; }

  .headline { position: absolute; left: 70px; top: 246px; }
  .headline h1 { font-size: 44px; font-weight: 600; letter-spacing: 2.6px; line-height: 1; color: var(--ink); }
  .headline p { margin-top: 14px; font-size: 17.5px; font-weight: 500; letter-spacing: 1.7px; color: var(--ink); }

  .cta {
    position: absolute; left: 71px; top: 357px; width: 204px; height: 60px;
    background: var(--ink); color: var(--white); text-decoration: none;
    display: flex; align-items: center; justify-content: center;
    font-size: 17px; font-weight: 500; letter-spacing: 1.6px;
  }
</style>
</head>
<body>
  <section class="hero">
    <div class="hero-photo" role="img" aria-label="Soft-focus sunlit garden background above a weathered wooden table"></div>
    <div class="hero-object" role="img" aria-label="Glass jar filled with coins with a green seedling sprouting from the top"></div>

    <header>
      <div class="brand">
        <span class="brand-mark"></span>
        <span class="brand-name">
          <span class="word">CORVANE</span>
          <span class="sub">ASSET MANAGEMENT</span>
        </span>
      </div>
      <a class="investor-login" href="#">INVESTOR LOGIN</a>
      <nav class="main-nav">
        <a href="#">ABOUT</a><span class="sep">|</span>
        <a href="#">INVESTMENTS</a><span class="sep">|</span>
        <a href="#">INSIGHTS</a><span class="sep">|</span>
        <a href="#">RESOURCES</a><span class="sep">|</span>
        <a href="#">CONTACT</a>
      </nav>
    </header>

    <div class="headline">
      <h1>$1.5 BILLION DOLLARS’</h1>
      <p>WORTH OF SUCCESSFUL TRANSACTIONS TO DATE</p>
    </div>
    <a class="cta" href="#">LEARN MORE</a>
  </section>
</body>
</html>
```